Business Card design for law firm = Brindlecourt Australia

We are seeking a new design for our business cards.
We are keeping our logo, which is attached.
We need space for
Name
Title
Address is , which is
Level 14
83 Tarrenby Street
Sydney NSW 2000
Phone :
Mobile :
Fax :
Email :
DX :
website www.brindlecourt.com.au

Industry/Entity Type

Law Firm / Banking and Finance

Contact Information for Business Card

We are seeking a new design for our business cards. We are keeping our logo. We need space for Name Title Address is Level 14 83 Tarrenby Street Sydney NSW 2000 Phone Mobile Fax Email DX website www.brindlecourt.com.au

Colors
0054AA
0677BA
7BADD7
CADEEF
E8F1F8

Requirements
Must have
• see our website for general feel www.brindlecourt.com.au

```html
<!DOCTYPE html>
<html lang="en">
<head>
<meta charset="utf-8">
<title>Brindlecourt Australia – Business Card</title>
<link rel="stylesheet" href="https://fonts.googleapis.com/css2?family=Montserrat:wght@400;500;700;800&display=swap">
<style>
  :root {
    --backdrop: #1f2224;
    --brand-blue: #2160ae;
    --accent-blue: #0677ba;
    --paper: #ffffff;
    --ink: #1b1b1b;
    --font-main: "Montserrat", Arial, sans-serif;
  }
  * { box-sizing: border-box; margin: 0; padding: 0; }
  html, body { width: 1200px; height: 1000px; overflow: hidden; }
  body { background: var(--backdrop); font-family: var(--font-main); position: relative; }

  .card {
    position: absolute;
    width: 540px;
    height: 310px;
    overflow: hidden;
    box-shadow: 0 14px 30px rgba(0,0,0,.45);
  }

  /* Front */
  .card-front { left: 90px; top: 110px; background: var(--brand-blue); }
  .front-panel { position: absolute; background: var(--paper); }
  .front-panel--top-right { left: 400px; top: 28px; width: 124px; height: 100px; }
  .front-panel--bottom-left { left: 18px; top: 188px; width: 124px; height: 100px; }
  .front-panel--center {
    left: 160px; top: 64px; width: 224px; height: 186px;
    display: flex; align-items: center; justify-content: center; gap: 12px;
  }

  .brand { display: flex; align-items: center; gap: 10px; }
  .brand-square { width: 34px; height: 34px; background: var(--accent-blue); flex: none; }
  .brand-name { font-weight: 500; color: var(--brand-blue); font-size: 22px; letter-spacing: .2px; }

  /* Back */
  .card-back { left: 570px; top: 570px; background: var(--paper); }
  .back-band {
    position: absolute; left: 0; top: 150px; width: 100%; height: 128px;
    background: var(--brand-blue);
  }
  .back-brand { position: absolute; right: 22px; top: 22px; }
  .back-brand .brand-square { width: 24px; height: 24px; }
  .back-brand .brand-name { font-size: 15px; }

  .holder { position: absolute; left: 26px; top: 52px; width: 220px; }
  .holder-name { font-weight: 800; font-size: 22px; color: var(--accent-blue); letter-spacing: .5px; line-height: 1; }
  .holder-title {
    font-size: 9px; font-weight: 500; color: var(--ink); text-transform: uppercase;
    padding: 3px 0 4px; border-bottom: 1.5px solid var(--accent-blue);
  }
  .holder-address { font-size: 11px; color: var(--ink); line-height: 1.45; margin-top: 5px; }

  .contact-list { position: absolute; left: 26px; top: 164px; list-style: none; }
  .contact-item {
    display: flex; align-items: center; gap: 10px;
    color: var(--paper); font-size: 11px; height: 21px;
  }
  .contact-icon { width: 13px; height: 13px; flex: none; display: flex; align-items: center; justify-content: center; }
  .contact-icon--label { font-size: 10px; font-weight: 500; width: 20px; }
  .contact-icon svg { width: 13px; height: 13px; }
</style>
</head>
<body>

<section class="card card-front" aria-label="Business card front">
  <div class="front-panel front-panel--top-right"></div>
  <div class="front-panel front-panel--bottom-left"></div>
  <div class="front-panel front-panel--center">
    <div class="brand">
      <span class="brand-square"></span>
      <span class="brand-name">Brindlecourt</span>
    </div>
  </div>
</section>

<section class="card card-back" aria-label="Business card back">
  <div class="back-band"></div>

  <div class="brand back-brand">
    <span class="brand-square"></span>
    <span class="brand-name">Brindlecourt</span>
  </div>

  <div class="holder">
    <p class="holder-name">NAME</p>
    <p class="holder-title">Managing Director</p>
    <p class="holder-address">Level 14, 83 Tarrenby Street<br>Sydney NSW 2000</p>
  </div>

  <ul class="contact-list">
    <li class="contact-item">
      <span class="contact-icon">
        <svg viewBox="0 0 16 16"><circle cx="8" cy="8" r="8" fill="#fff"/><path d="M5.5 4.5l1.6 1.8-.8 1.1c.5 1 1.2 1.7 2.2 2.2l1.1-.8 1.8 1.6-.9 1.1c-2.8-.4-4.9-2.5-5.3-5.3z" fill="var(--brand-blue)"/></svg>
      </span>
      02 9170 4385
    </li>
    <li class="contact-item">
      <span class="contact-icon">
        <svg viewBox="0 0 16 16"><rect x="4" y="2" width="8" height="5" fill="#fff"/><rect x="1" y="6" width="14" height="7" rx="1.5" fill="#fff"/><rect x="4" y="10" width="8" height="1.4" fill="var(--brand-blue)"/></svg>
      </span>
      02 9170 4386
    </li>
    <li class="contact-item">
      <span class="contact-icon">
        <svg viewBox="0 0 16 16"><rect x="1" y="3" width="14" height="10" fill="#fff"/><path d="M1 3l7 6 7-6" fill="none" stroke="var(--brand-blue)" stroke-width="1.3"/></svg>
      </span>
      enquiries@brindlecourt.com.au
    </li>
    <li class="contact-item">
      <span class="contact-icon contact-icon--label">DX</span>
      318 Sydney
    </li>
    <li class="contact-item">
      <span class="contact-icon">
        <svg viewBox="0 0 16 16"><circle cx="8" cy="8" r="7" fill="none" stroke="#fff" stroke-width="1.4"/><ellipse cx="8" cy="8" rx="3" ry="7" fill="none" stroke="#fff" stroke-width="1.2"/><line x1="1" y1="8" x2="15" y2="8" stroke="#fff" stroke-width="1.2"/></svg>
      </span>
      www.brindlecourt.com.au
    </li>
  </ul>
</section>

</body>
</html>
```